Business card for acupunctist in Melbourne. Specialises in Fertility, pre and post natal care, pain

I am looking for a business card which is going to catch people eyes. Two sided, one side in a muted colour (keeping it feminine) (pink or yellow???)maybe with a little simple logo or picture, the other side I was thinking white with 3 colours (pink grey and yellow... Had these in mind.
Info on the card
Maren Quillby Acupuncture

Dr Maren Quillby (TCM Acupuncture)
Acupuncture for balancing body and mind.
Verdant Osprey Clinic
14 Corran Lane, Eastwood 3071.
96274158
0438215074
Marentcm@quorvenmail.com

Some other little logo/ designs I have liked are as follows:
http://www.tessrolfeclinic.com/rates-and-insurance/
http://www.corabethwinslow.com/
http://www.zd-needlework.co.uk/

Target Market(s)

professional women, people in pain, active people, people seeking a healthy lifefstyle.

Industry/Entity Type

Business

Font styles to use
Serif
Sans Serif

Colors
eea4c8
fde08a
aaaaaa

Requirements
Must have
• Must be eye catching, but not too loud and busy. Subltle is good. Simple is also good. The logo could be something that represents growth and health and nurturing. Again not too elaborate, very simple.
Thankyou
Should not have
• Electric colours, crazy fonts, Pictures of yin and yang, candles, or bodies.

```html
<!DOCTYPE html>
<html lang="en">
<head>
<meta charset="utf-8">
<title>Maren Quillby Acupuncture – Business Card</title>
<link rel="stylesheet" href="https://fonts.googleapis.com/css2?family=Fenix&family=Roboto+Condensed:wght@300;400&display=swap">
<style>
  :root {
    --sun: #fdf200;
    --blush: #f59ad3;
    --blush-light: #fbb0f0;
    --ink: #0a0a0a;
    --slate: #939393;
    --label-grey: #555555;
    --paper: #ffffff;
    --sans: "Roboto Condensed", Arial, sans-serif;
    --serif: "Fenix", Georgia, serif;
  }
  html, body {
    margin: 0;
    padding: 0;
    width: 840px;
    height: 1200px;
    overflow: hidden;
    background: var(--paper);
  }
  .sheet {
    position: relative;
    width: 840px;
    height: 1200px;
    overflow: hidden;
    font-family: var(--sans);
  }
  .card-front {
    position: absolute;
    left: 0; top: 0;
    width: 840px; height: 534px;
    background: var(--sun);
    overflow: hidden;
  }
  .card-front svg { display: block; }
  .divider {
    position: absolute;
    left: 0;
    width: 840px;
    height: 14px;
    background: var(--ink);
  }
  .divider--front { top: 534px; }
  .divider--back { top: 706px; }
  .side-label {
    position: absolute;
    left: 0; width: 840px;
    text-align: center;
    font-family: var(--sans);
    font-weight: 300;
    font-size: 37px;
    color: var(--label-grey);
    margin: 0;
    line-height: 1;
  }
  .side-label--front { top: 551px; }
  .side-label--back { top: 662px; }
  .card-back {
    position: absolute;
    left: 0; top: 720px;
    width: 840px; height: 480px;
    overflow: hidden;
  }
  .practitioner {
    position: absolute;
    left: 40px; top: 76px;
    margin: 0;
    font-family: var(--serif);
    font-weight: 400;
    font-size: 38px;
    color: var(--blush-light);
    line-height: 1;
    white-space: nowrap;
  }
  .tagline {
    position: absolute;
    left: 41px; top: 121px;
    margin: 0;
    font-family: var(--sans);
    font-weight: 300;
    font-size: 33px;
    color: var(--slate);
    line-height: 1;
    white-space: nowrap;
  }
  .contact-panel {
    position: absolute;
    left: 0; top: 180px;
    width: 370px; height: 182px;
    background: var(--slate);
    border-radius: 0 3px 3px 0;
    box-sizing: border-box;
    padding: 17px 0 0 41px;
  }
  .contact-panel p {
    margin: 0;
    font-family: var(--sans);
    font-weight: 300;
    font-size: 25px;
    line-height: 27px;
    color: var(--sun);
    white-space: nowrap;
  }
  .contact-panel .email {
    color: var(--paper);
    margin-top: 6px;
    font-size: 24px;
  }
  .back-mark {
    position: absolute;
    left: 508px; top: 176px;
  }
</style>
</head>
<body>
<main class="sheet">
  <section class="card-front" aria-label="Card front">
    <svg width="840" height="534" viewBox="0 0 840 534">
      <g class="guide-lines" fill="none" stroke-width="3">
        <g stroke="var(--blush)" transform="translate(-3,2)">
          <line x1="176" y1="0" x2="552" y2="486"/>
          <line x1="312" y1="0" x2="840" y2="344"/>
          <line x1="480" y1="0" x2="840" y2="340"/>
          <line x1="316" y1="444" x2="840" y2="100"/>
          <line x1="264" y1="340" x2="336" y2="534"/>
        </g>
        <g stroke="var(--paper)">
          <line x1="176" y1="0" x2="552" y2="486"/>
          <line x1="312" y1="0" x2="840" y2="344"/>
          <line x1="480" y1="0" x2="840" y2="340"/>
          <line x1="316" y1="444" x2="840" y2="100"/>
          <line x1="264" y1="340" x2="336" y2="534"/>
        </g>
      </g>
      <g class="wordmark" font-family="Roboto Condensed, Arial, sans-serif" font-weight="300" font-size="118">
        <g fill="var(--blush)" transform="translate(-4,3)">
          <text x="272" y="208" transform="rotate(-37 272 208)" textLength="262" lengthAdjust="spacingAndGlyphs">Maren</text>
          <text x="296" y="308" transform="rotate(-38 296 308)" textLength="356" lengthAdjust="spacingAndGlyphs">Quillby</text>
          <text x="290" y="416" transform="rotate(-34.5 290 416)" textLength="616" lengthAdjust="spacingAndGlyphs">Acupuncture</text>
        </g>
        <g fill="var(--paper)">
          <text x="272" y="208" transform="rotate(-37 272 208)" textLength="262" lengthAdjust="spacingAndGlyphs">Maren</text>
          <text x="296" y="308" transform="rotate(-38 296 308)" textLength="356" lengthAdjust="spacingAndGlyphs">Quillby</text>
          <text x="290" y="416" transform="rotate(-34.5 290 416)" textLength="616" lengthAdjust="spacingAndGlyphs">Acupuncture</text>
        </g>
      </g>
      <g class="brand-mark">
        <circle cx="130" cy="242" r="97" fill="none" stroke="var(--blush)" stroke-width="14"/>
        <text x="130" y="250" text-anchor="middle" font-family="Roboto Condensed, Arial, sans-serif" font-weight="400" font-size="26" fill="var(--blush)">Maren Quillby</text>
      </g>
    </svg>
  </section>

  <div class="divider divider--front"></div>
  <p class="side-label side-label--front">Front</p>
  <p class="side-label side-label--back">Back</p>
  <div class="divider divider--back"></div>

  <section class="card-back" aria-label="Card back">
    <h1 class="practitioner">Dr Maren Quillby (TCM Acupuncture)</h1>
    <p class="tagline">Acupuncture for balancing body and mind.</p>
    <address class="contact-panel">
      <p>Verdant Osprey Clinic</p>
      <p>14 Corran Lane, Eastwood 3071.</p>
      <p>96274158</p>
      <p>0438215074</p>
      <p class="email">Marentcm@quorvenmail.com</p>
    </address>
    <svg class="back-mark" width="332" height="304" viewBox="0 0 332 304">
      <circle cx="176" cy="180" r="168" fill="none" stroke="var(--blush-light)" stroke-width="16"/>
      <text x="176" y="190" text-anchor="middle" font-family="Roboto Condensed, Arial, sans-serif" font-weight="400" font-size="36" fill="var(--blush-light)">Maren Quillby</text>
    </svg>
  </section>
</main>
</body>
</html>
```